Two Web Pages Design for an Anti-Aging Med Spa

Hi,
We are looking to redesign our website which is an Medspa in the Anti-Aging and Hormone Replacement business. We only need two pages designed. Frontpage and one inner page. and we need professional clean looks with matching colors to our logo (see attached files).
Sites we like:
http://velmorabeauty.example/
http://www.brindlequartz.example/

Target Market(s)

Mid-Age Men and Women

Industry/Entity Type

Business

Number of Pages Required

2 page

Font styles to use
Sans Serif

Colors
86cfc6
33b7a4
33a6d7
85cae6
ffffff
cadf82
9bcb3b
fde08a

Requirements
Must have
• IMPORTANT: YOU WOULD ONLY NEED TO DESIGN THE FRONTPAGE AND ONE INNER PAGE, NOT THE WHOLE SITE. FRONT-PAGE MUST INCLUDE A SLIDER. If you have any other questions please PM me.

```html
<!DOCTYPE html>
<html lang="en">
<head>
<meta charset="utf-8">
<title>Lumavera – Anti-Aging Med Spa</title>
<link href="https://fonts.googleapis.com/css2?family=Questrial&family=Montserrat:wght@400;600;700&family=Open+Sans:ital,wght@0,400;0,600;1,400&display=swap" rel="stylesheet">
<style>
:root{
  --teal:#33b7a4;
  --teal-soft:#86cfc6;
  --teal-light:#5cc6b6;
  --lime:#9bcb3b;
  --lime-soft:#cadf82;
  --ink:#3d3d3d;
  --muted:#666;
  --white:#fff;
  --line:#cfd8d6;
}
*{box-sizing:border-box;margin:0;padding:0}
html,body{width:846px;height:1200px;overflow:hidden;background:var(--white)}
body{position:relative;font-family:"Open Sans",Arial,sans-serif;color:var(--ink)}
.abs{position:absolute}

/* top bar */
.topbar{left:0;top:0;width:846px;height:20px;background:var(--teal);color:var(--white);font-family:"Montserrat",sans-serif;font-size:7px;font-weight:600}
.topbar .phone{left:388px;top:4px;font-size:9px;display:flex;align-items:center;gap:3px;white-space:nowrap}
.topbar .tab{top:0;height:20px;line-height:20px;padding:0 6px;display:flex;align-items:center;gap:3px;white-space:nowrap}
.topbar .tab.active{background:var(--teal-light)}
.topbar .social{top:4px;width:13px;height:13px;border:1px solid rgba(255,255,255,.8);border-radius:50%}

/* header */
.brand{left:113px;top:36px;display:flex;align-items:center;gap:6px;font-family:"Questrial",sans-serif;font-size:15px;color:var(--teal)}
.brand .dot{width:12px;height:12px;border-radius:50%;background:var(--lime)}
.nav{left:221px;top:45px;display:flex;gap:13px;font-family:"Montserrat",sans-serif;font-size:7.9px;font-weight:600;color:#555;white-space:nowrap}

/* slider */
.slider{left:0;top:77px;width:846px;height:278px;background:linear-gradient(100deg,#d9d6d2 0%,#bdb9b4 35%,#8e8a86 55%,#cfcbc6 75%,#a9a29b 100%)}
.slider .arrow{top:125px;width:28px;height:28px;border-radius:50%;background:rgba(120,120,120,.55)}
.slide-caption{left:422px;top:80px;width:90px;text-align:center;font-family:"Montserrat",sans-serif;white-space:nowrap}
.slide-caption b{display:block;color:var(--teal);font-size:10px;line-height:12px;font-weight:700}
.slide-caption span{display:block;color:#222;font-size:6px;line-height:9px;font-weight:700}
.slide-text{left:558px;top:124px;width:110px;font-size:8.5px;line-height:12.5px;font-style:italic;color:#333}

/* bubbles */
.bubble{width:80px;height:80px;border-radius:50%;background:var(--teal-soft);color:var(--white);font-family:"Questrial",sans-serif;text-align:center;line-height:20px;padding-top:21px;font-size:15px}
.bubble .second{font-size:18px}
.bubble::after{content:"";position:absolute;right:8px;bottom:-4px;border-left:10px solid transparent;border-top:12px solid var(--teal-soft);transform:rotate(-20deg)}

/* welcome */
.welcome-name{left:197px;top:394px;font-family:"Questrial",sans-serif;font-size:16px;color:#444;white-space:nowrap}
.welcome-name em{font-style:normal;color:var(--lime);font-size:18px}
.welcome-title{left:197px;top:415px;font-family:"Questrial",sans-serif;font-size:16.5px;font-weight:700;color:var(--teal);white-space:nowrap}
.welcome-copy{left:197px;top:442px;width:520px;font-size:8.6px;line-height:15px;color:#555}

/* services */
.service{top:502px;height:163px;overflow:hidden}
.service .band{position:absolute;left:0;right:0;top:86px;height:52px;background:rgba(255,255,255,.72);font-family:"Questrial",sans-serif;color:var(--lime);line-height:1;white-space:nowrap}
.service .band .big{position:absolute;font-size:25px}
.service .band .small{position:absolute;font-size:16px}

/* newsletter */
.signup{left:0;top:745px;width:846px;height:78px;background:var(--teal);color:var(--white)}
.signup .tag{left:148px;top:37px;width:112px;text-align:center;font-size:10px;line-height:15px}
.signup .lead{left:273px;top:15px;font-size:9.5px;white-space:nowrap}
.field{background:var(--white);border:1px solid var(--line);font-size:7px;color:#888;padding-left:6px;display:flex;align-items:center;white-space:nowrap}
.signup .field{font-style:italic}
.signup .submit{left:679px;top:39px;width:52px;height:23px;background:var(--teal-soft);font-family:"Montserrat",sans-serif;font-size:9px;font-weight:600;display:flex;align-items:center;justify-content:center}

/* testimonial */
.quote-mark{font-family:Georgia,serif;font-size:40px;color:var(--teal-soft);line-height:1}
.quote-lead{left:131px;top:889px;width:380px;font-family:"Questrial",sans-serif;font-size:18px;line-height:21px;color:#222}
.quote-sub{left:133px;top:940px;font-family:"Questrial",sans-serif;font-weight:700;font-size:15.5px;color:var(--teal);white-space:nowrap}
.quote-body{left:138px;top:966px;width:330px;font-size:8.6px;line-height:15px;font-style:italic;color:#555}
.quote-author{left:139px;top:1027px;font-family:"Montserrat",sans-serif;font-weight:600;font-size:9px;color:var(--teal)}

/* consultation form */
.consult{left:520px;top:856px;width:212px;height:221px;border:1px solid var(--teal)}
.consult .head{height:42px;background:var(--teal);color:var(--white);font-family:"Questrial",sans-serif;padding:10px 0 0 12px;font-size:10.5px;white-space:nowrap}
.consult .head strong{font-family:"Montserrat",sans-serif;font-size:19px;font-weight:700}
.consult .field{position:absolute;height:22px;border-radius:2px}
.consult .select::after{content:"";position:absolute;right:6px;top:6px;width:9px;height:9px;border:1px solid #555}
.consult .select b{position:absolute;right:8px;top:10px;border-left:3px solid transparent;border-right:3px solid transparent;border-top:3px solid #333}
.consult .send{position:absolute;left:11px;top:183px;width:189px;height:27px;border-radius:2px;background:var(--teal);color:var(--white);font-family:"Montserrat",sans-serif;font-weight:600;font-size:11px;display:flex;align-items:center;justify-content:center}

/* footer */
.footer{left:0;top:1120px;width:846px;height:80px;background:var(--teal);color:var(--white)}
.footer h4{position:absolute;font-family:"Montserrat",sans-serif;font-weight:600;font-size:10px;display:flex;align-items:center;gap:5px;white-space:nowrap}
.footer p{position:absolute;font-size:8.5px;line-height:13px}
.footer .address{font-style:italic}
.footer .circle{top:21px;width:18px;height:18px;border:1px solid var(--white);border-radius:50%}
.footer .legal{left:569px;top:45px;font-size:6.8px;white-space:nowrap}
</style>
</head>
<body>

<div class="abs topbar">
  <div class="abs phone">
    <svg width="7" height="9" viewBox="0 0 7 9"><path d="M1 1h2l.5 2-1 .8a5 5 0 0 0 2 2.4l.8-1 1.7.6V8H5A5 5 0 0 1 0 3V1z" fill="#fff"/></svg>
    555 - 014 - 2290
  </div>
  <div class="abs tab active" style="left:480px">
    <svg width="7" height="6" viewBox="0 0 7 6"><path d="M3.5 0 7 3H6v3H4.3V4H2.7v2H1V3H0z" fill="#fff"/></svg>Home
  </div>
  <div class="abs tab" style="left:527px">
    <svg width="6" height="6" viewBox="0 0 6 6"><circle cx="3" cy="1.6" r="1.5" fill="#fff"/><path d="M0 6a3 2.5 0 0 1 6 0z" fill="#fff"/></svg>About Us
  </div>
  <div class="abs tab" style="left:585px">
    <svg width="7" height="5" viewBox="0 0 7 5"><rect width="7" height="5" fill="#fff"/><path d="M0 0l3.5 2.7L7 0" stroke="#33b7a4" fill="none" stroke-width=".8"/></svg>Contact Us
  </div>
  <span class="abs social" style="left:656px"></span>
  <span class="abs social" style="left:677px"></span>
  <span class="abs social" style="left:697px"></span>
  <span class="abs social" style="left:717px"></span>
</div>

<div class="abs brand"><span class="dot"></span>Lumavera</div>
<nav class="abs nav">
  <span>REPLACEMENT</span><span>REJUVENATION</span><span>WEIGHT AND HEALTH</span><span>BLOG</span><span>SHOP</span><span>TESTIMONIALS</span><span>NEWSLETTER SIGNUP</span>
</nav>

<div class="abs slider" role="img" aria-label="Photo of a treatment room with a reclining treatment chair, wall poster and vanity counter">
  <span class="abs arrow" style="left:83px">
    <svg width="28" height="28" viewBox="0 0 28 28"><path d="M16 9l-5 5 5 5" stroke="#fff" stroke-width="2.2" fill="none"/></svg>
  </span>
  <span class="abs arrow" style="left:733px">
    <svg width="28" height="28" viewBox="0 0 28 28"><path d="M12 9l5 5-5 5" stroke="#fff" stroke-width="2.2" fill="none"/></svg>
  </span>
  <div class="abs slide-caption"><b>HORMONE</b><span>REPLACEMENT</span></div>
  <p class="abs slide-text">Lorem ipsum dolor sit amet, consectetur adipi-scing elit, sed do eiusmod tempor incididunt ut</p>
</div>

<div class="abs bubble" style="left:115px;top:317px">Welcome<br><span class="second">To..</span></div>
<div class="abs welcome-name"><em>L</em>umavera</div>
<h1 class="abs welcome-title">Eiusmod tempor incididunt ut labore et dolore</h1>
<p class="abs welcome-copy">Consectetur adipiscing elit, sed do eiusmod tempor incididunt ut labore et dolore magna aliqua. Ut enim ad minim veniam, quis nostrud exercitation ullamco laboris nisi ut aliquip ex ea commodo consequat. Duis aute irure dolor in reprehenderit.</p>

<div class="abs service" style="left:113px;width:143px;background:linear-gradient(135deg,#d8c2b0,#b98d6f 55%,#eadfd6)" role="img" aria-label="Photo of a smiling mature couple">
  <div class="band"><span class="big" style="left:9px;top:9px">Hormone</span><span class="small" style="left:40px;top:32px">Replacement</span></div>
</div>
<div class="abs service" style="left:272px;width:301px;background:linear-gradient(120deg,#e9d2c4,#d9b6a2 50%,#f1e4da)" role="img" aria-label="Close-up photo of a cosmetic lip injection treatment">
  <div class="band" style="top:97px;height:50px"><span class="big" style="left:10px;top:12px">Rejuvenation</span></div>
</div>
<div class="abs service" style="left:589px;width:143px;background:linear-gradient(160deg,#6b4030,#c98f6e 50%,#3e2a24)" role="img" aria-label="Photo of a tape measure around a slim waist">
  <div class="band"><span class="big" style="left:9px;top:9px">Weight</span><span class="small" style="left:48px;top:33px">and Health</span></div>
</div>

<section class="abs signup">
  <p class="abs tag">Monthly Special<br>Offers, News, &amp; Advice.</p>
  <p class="abs lead">Subscribe to our Newsletter to Keep up with the latest Skin Clinic news and Special Offers...</p>
  <div class="abs field" style="left:273px;top:39px;width:195px;height:23px">Name</div>
  <div class="abs field" style="left:474px;top:39px;width:199px;height:23px">Email</div>
  <div class="abs submit">SUBMIT</div>
</section>
<div class="abs bubble" style="left:128px;top:697px;font-size:18px">Sign<br>Up..</div>

<span class="abs quote-mark" style="left:112px;top:874px">&ldquo;</span>
<p class="abs quote-lead">Lorem ipsum dolor sit amet, consectetur adipiscing elit, sed do eiusmod</p>
<h2 class="abs quote-sub">Duis aute irure dolor in reprehe voluptate</h2>
<p class="abs quote-body">Lorem ipsum dolor sit amet, consectetur adipiscing elit, sed do eiusmod tempor incididunt ut labore et dolore magna aliqua. Ut enim ad minim veniam, quis nostrud exercitation.</p>
<span class="abs quote-mark" style="left:223px;top:996px">&rdquo;</span>
<p class="abs quote-author">Harlan Whitcombe</p>

<aside class="abs consult">
  <div class="head"><strong>FREE SKIN</strong> Consultation</div>
  <div class="field" style="left:11px;top:55px;width:89px">Name</div>
  <div class="field" style="left:107px;top:55px;width:94px">Email Address</div>
  <div class="field" style="left:11px;top:87px;width:189px">Phone Number</div>
  <div class="field select" style="left:11px;top:119px;width:189px">Location<b></b></div>
  <div class="field select" style="left:11px;top:151px;width:189px">Service of Interest<b></b></div>
  <div class="send">Submit</div>
</aside>

<footer class="abs footer">
  <h4 style="left:113px;top:20px">
    <svg width="11" height="8" viewBox="0 0 11 8"><rect width="11" height="8" fill="#fff"/><path d="M0 0l5.5 4.3L11 0" stroke="#33b7a4" fill="none"/></svg>Contact info
  </h4>
  <p class="address" style="left:130px;top:37px;width:118px">22,Lorem ipsum dolor sit amet, consectetur adipiscing</p>
  <h4 style="left:292px;top:20px">
    <svg width="7" height="10" viewBox="0 0 7 10"><path d="M1 1h2l.6 2-1.2.9a5 5 0 0 0 2 3l.9-1 1.7.7V9H5A5 5 0 0 1 0 4V1z" fill="#fff"/></svg>Phone
  </h4>
  <p style="left:305px;top:38px">555 - 014 - 2290</p>
  <h4 style="left:414px;top:20px">
    <svg width="11" height="8" viewBox="0 0 11 8"><rect width="11" height="8" fill="#fff"/><path d="M0 0l5.5 4.3L11 0" stroke="#33b7a4" fill="none"/></svg>Email
  </h4>
  <p style="left:430px;top:38px">info@lumavera.example</p>
  <span class="abs circle" style="left:569px"></span>
  <span class="abs circle" style="left:597px"></span>
  <span class="abs circle" style="left:624px"></span>
  <span class="abs circle" style="left:652px"></span>
  <p class="legal">&copy;2014 lumavera.example. All Rights Reserved.</p>
</footer>

</body>
</html>
```